Book Cover for Christian Book titled, "Climbing Past the Silver Hills"

Size of book cover will be 6" x 9".
The book is about how a person can know beyond a shadow of a doubt that they will go to heaven when they die.
The Title is "Climbing Past the Silver Hills"
Subtitle is "Finding Lasting Peace Through Daily Quiet Prayer and Reflection."
The front of the book should have title, subtitle, and author. The back of the book and spine should have no text and be a solid color.
The uploaded pic is a possibility for a design; but I'm open to other designs.
Whatever images are used need to be very high quality to meet Marrowind Folio Services guidelines. Also, the finished product needs to be sized to match the MFS guide for a 6x9 book.

```html
<!DOCTYPE html>
<html lang="en">
<head>
<meta charset="utf-8">
<title>Climbing Past the Silver Hills – Book Cover</title>
<link rel="stylesheet" href="https://fonts.googleapis.com/css2?family=Bebas+Neue&family=Poppins:wght@300&display=swap">
<style>
  :root {
    --page-bg: #ffffff;
    --sky-deep: #0a2470;
    --sky-blue: #1c63c6;
    --sky-light: #3fa6e0;
    --sun-glow: #f6ec62;
    --horizon-gold: #e9d64a;
    --field-light: #3b9427;
    --field-dark: #1c5512;
    --title-ink: #f2f2f2;
    --text-ink: #ffffff;
  }
  * { margin: 0; padding: 0; box-sizing: border-box; }
  html, body {
    width: 1200px;
    height: 827px;
    overflow: hidden;
    background: var(--page-bg);
  }
  .stage {
    width: 1200px;
    height: 827px;
    display: flex;
    align-items: center;
    justify-content: center;
  }
  .book-cover {
    position: relative;
    width: 520px;
    height: 780px;
    overflow: hidden;
  }
  .cover-scene {
    position: absolute;
    inset: 0;
    width: 100%;
    height: 100%;
  }
  .cover-title {
    position: absolute;
    top: 62px;
    left: 0;
    right: 0;
    padding-left: 22px;
    text-align: center;
    font-family: "Bebas Neue", "Oswald", sans-serif;
    color: var(--title-ink);
    line-height: 0.9;
    text-shadow: 0 2px 6px rgba(0, 20, 60, 0.25);
  }
  .cover-title .line-top { display: block; font-size: 84px; }
  .cover-title .line-mid { display: block; font-size: 104px; }
  .cover-title .line-end { display: block; font-size: 122px; }
  .cover-subtitle {
    position: absolute;
    top: 626px;
    left: 50%;
    transform: translateX(-50%);
    width: 420px;
    padding-left: 10px;
    text-align: center;
    font-family: "Poppins", sans-serif;
    font-weight: 300;
    font-size: 19px;
    line-height: 1.5;
    color: var(--text-ink);
  }
  .cover-author {
    position: absolute;
    top: 734px;
    left: 0;
    right: 0;
    text-align: center;
    font-family: "Poppins", sans-serif;
    font-weight: 300;
    font-size: 14px;
    letter-spacing: 15px;
    padding-left: 22px;
    color: var(--text-ink);
  }
</style>
</head>
<body>
  <main class="stage">
    <section class="book-cover">
      <svg class="cover-scene" viewBox="0 0 520 780" preserveAspectRatio="none" role="img" aria-label="Photograph of a bright sun bursting through blue and golden clouds above a wide green field with a line of trees on the horizon">
        <defs>
          <linearGradient id="sky" x1="0" y1="0" x2="0" y2="1">
            <stop offset="0" stop-color="var(--sky-deep)"/>
            <stop offset="0.3" stop-color="var(--sky-blue)"/>
            <stop offset="0.5" stop-color="var(--sky-light)"/>
            <stop offset="0.64" stop-color="var(--sun-glow)"/>
            <stop offset="0.72" stop-color="var(--horizon-gold)"/>
            <stop offset="0.73" stop-color="var(--field-light)"/>
            <stop offset="1" stop-color="var(--field-dark)"/>
          </linearGradient>
          <radialGradient id="sun" cx="0.7" cy="0.6" r="0.35">
            <stop offset="0" stop-color="#ffffff" stop-opacity="0.95"/>
            <stop offset="0.25" stop-color="#fbf48a" stop-opacity="0.7"/>
            <stop offset="1" stop-color="#fbf48a" stop-opacity="0"/>
          </radialGradient>
        </defs>
        <rect width="520" height="780" fill="url(#sky)"/>
        <rect width="520" height="565" fill="url(#sun)"/>
      </svg>

      <h1 class="cover-title">
        <span class="line-top">Climbing Past</span>
        <span class="line-mid">The Silver</span>
        <span class="line-end">Hills</span>
      </h1>

      <p class="cover-subtitle">Finding Lasting Peace Through Daily Quiet Prayer and Reflection.</p>

      <p class="cover-author">AUTHOR NAME</p>
    </section>
  </main>
</body>
</html>
```